wardrobe/costume stylist needs good business card for own business

Hi:)

I'm wanting a business card for my company. I am a freelance stylist.

I do wardrobe/costume stylist to TV commercials; Films; Fashion and Lifestyle shoots.

I'd like a design based around my name Rosalind Pember written nicely, maybe a colour? Up to you?!

I've attached a couple of images of business cards I like
.... be creative and have fun!

Thank you :)
Updates

Reason: I was trying to get my new business card ready for before I headed overseas Friday morning but I don't think that was realistic so I'd like to extend the deadline to give time to the project. Thank you

Hi designers:) Thank you for all your designs, I've extended the deadline until Sunday, so there's a bit more time. I've attached 3 pictures of business cards which I quite like, please take a look to see if it can be of help in your process. I like the pale plain or patterned background with dark font and the dark plain or patterned background with the pale font the motifs the feminine fonts the plain fonts I like the idea of playing with a circle or some shape on one side of the card with my name or initials as in the picture I have on my post could you play around with this idea a bit please? Thank you all for the work you've done :) Rosa

Hi I am working overseas til Saturday night sorry for no feedback until I teturn Thanks :) Rosa

Hi designers, Thank you all so much for submitting your designs, I really appreciate your input into my project :) I'm sorry I didn't get to respond to some comments, and give feedback. I didn't back from being away until later than I expected, and the deadline had passed then, so apologies. Thanks to you all again for all your really good designs :) Rosa

Target Market(s)

I am a freelance stylist my target audience is producers, production companies, photographers, directors...

Industry/Entity Type

Business

Requirements
Must have
• Rosalind Pember
Stylist or Wardrobe Stylist

email rosapember@quillnet.co.nz
Mobile 0218846193

(Don't have to use the words 'email' and 'mobile')
Nice to have
• Would like it to be double sided
Like B & W
Like pale colour background with dark font or white font
Like dark colour background with pale font
Should not have
• I would prefer it not to incorporate pictures

```html
<!DOCTYPE html>
<html lang="en">
<head>
<meta charset="utf-8">
<title>Rosalind Pember — Stylist Business Card</title>
<link rel="stylesheet" href="https://fonts.googleapis.com/css2?family=Encode+Sans+Condensed:wght@300&display=swap">
<style>
  :root {
    --page: #ffffff;
    --card: #d6d3b8;
    --ink-light: #ffffff;
    --ink-grey: #8a8a8a;
    --font-body: "Encode Sans Condensed", "Arial Narrow", sans-serif;
  }
  * { margin: 0; padding: 0; box-sizing: border-box; }
  html, body {
    width: 1000px;
    height: 1200px;
    overflow: hidden;
    background: var(--page);
  }
  .sheet {
    position: relative;
    width: 1000px;
    height: 1200px;
  }
  .card {
    position: absolute;
    left: 22px;
    width: 956px;
    height: 546px;
    background: var(--card);
  }
  .card--front { top: 44px; }
  .card--back { top: 612px; }

  .signature {
    position: absolute;
    font-family: var(--font-body);
    font-weight: 300;
    color: var(--ink-light);
    white-space: nowrap;
    line-height: 1;
  }
  .card--front .signature {
    left: 164px;
    top: 272px;
    font-size: 40px;
    letter-spacing: 2px;
    transform: translate(-50%, -50%) rotate(-90deg);
  }
  .card--back .signature {
    left: 478px;
    top: 273px;
    font-size: 72px;
    letter-spacing: 3px;
    transform: translate(-50%, -50%);
  }

  .contact {
    position: absolute;
    left: 475px;
    top: 162px;
    width: 400px;
    text-align: center;
    font-family: var(--font-body);
    font-weight: 300;
  }
  .contact__name {
    font-size: 54px;
    line-height: 1;
    color: var(--ink-light);
    letter-spacing: 0.5px;
  }
  .contact__role {
    margin-top: 12px;
    font-size: 34px;
    line-height: 1;
    color: var(--ink-light);
  }
  .contact__email {
    margin-top: 48px;
    font-size: 30px;
    line-height: 1;
    color: var(--ink-grey);
  }
  .contact__phone {
    margin-top: 18px;
    font-size: 31px;
    line-height: 1;
    color: var(--ink-grey);
    letter-spacing: 0.5px;
  }
</style>
</head>
<body>
<main class="sheet">
  <section class="card card--front">
    <p class="signature">Rosalind Pember</p>

    <div class="contact">
      <p class="contact__name">Rosalind Pember</p>
      <p class="contact__role">Stylist</p>
      <p class="contact__email">rosapember@quillnet.co.nz</p>
      <p class="contact__phone">0218846193</p>
    </div>
  </section>

  <section class="card card--back">
    <p class="signature">Rosalind Pember</p>
  </section>
</main>
</body>
</html>
```